QRN Law Letterhead

Want law firm letterhead - both in terms of a pdf file that I can use electronically as letterhead by adding it as a background - and in terms of a file that I can send to a company to create actual letterhead.
Industry/Entity Type
Law Firm
Font styles to use
Sans Serif
Requirements
Must have
- Should have the following information (you can decide where to place):
- My name - Emil Vostrakian
- My email - emil@qrnlegalgroup.example
- My address - 2861 Corvella Parkway 318-742
- San Jose, California 95342
- Website - www.qrnlegalgroup.example
- Phone - 408-297-1586
- Fax - 408-853-2941
- The logo I attached
Nice to have
- I think I would prefer to have a black and white color scheme.
- I don't necessarily need a title after my name, but I have seen a few design submissions that include a generic title. The title I would use is "IP Litigator & Trademark Attorney"

```html
<!DOCTYPE html>
<html lang="en">
<head>
<meta charset="utf-8">
<title>QRN Law Letterhead</title>
<link href="https://fonts.googleapis.com/css2?family=Open+Sans:wght@400;600;700&display=swap" rel="stylesheet">
<style>
  :root {
    --backdrop: #e3e4e3;
    --paper: #ffffff;
    --ink: #2b2f33;
    --slate: #5f7a8c;
    --slate-dark: #4d6576;
    --silver-light: #f2f2f2;
    --silver-dark: #a9abad;
    --rule: #b7bfc5;
  }
  * { margin: 0; padding: 0; box-sizing: border-box; }
  html, body {
    width: 1200px; height: 784px; overflow: hidden;
    background: var(--backdrop);
    font-family: "Open Sans", Arial, sans-serif;
  }
  .letterhead {
    position: absolute; left: 320px; top: 30px;
    width: 560px; height: 725px;
    background: var(--paper);
    box-shadow: 0 2px 10px rgba(0,0,0,0.12);
    overflow: hidden;
  }
  .masthead {
    position: absolute; left: 26px; top: 28px; right: 22px;
    display: flex; align-items: center; gap: 12px;
  }
  .brand { display: flex; align-items: center; gap: 7px; }
  .brand-mark {
    width: 24px; height: 24px; border-radius: 50%;
    border: 3px solid var(--slate);
  }
  .brand-name {
    font-size: 24px; font-weight: 600; color: var(--ink);
    letter-spacing: 0.2px; white-space: nowrap;
  }
  .divider { width: 1px; height: 36px; background: var(--rule); transform: skewX(-18deg); }
  .attorney { text-align: right; white-space: nowrap; }
  .attorney-name { font-size: 11px; font-weight: 700; color: var(--slate); }
  .attorney-title { font-size: 7.5px; color: var(--ink); }
  .contact { font-size: 6.6px; line-height: 1.6; color: var(--ink); white-space: nowrap; }
  .contact-line { display: flex; align-items: center; gap: 8px; }
  .contact-address { color: var(--slate); font-weight: 600; }
  .contact-item { display: inline-flex; align-items: center; gap: 3px; }
  .contact-icon { width: 6px; height: 6px; fill: var(--slate); flex: none; }
  .footer-wave { position: absolute; left: 0; bottom: 0; width: 560px; height: 140px; }
</style>
</head>
<body>
  <main class="letterhead">
    <header class="masthead">
      <div class="brand">
        <span class="brand-mark"></span>
        <span class="brand-name">QRN Law</span>
      </div>
      <span class="divider"></span>
      <div class="attorney">
        <div class="attorney-name">Emil Vostrakian</div>
        <div class="attorney-title">IP Litigator &amp; Trademark Attorney</div>
      </div>
      <span class="divider"></span>
      <div class="contact">
        <div class="contact-line contact-address">
          <span class="contact-item">
            <svg class="contact-icon" viewBox="0 0 10 10"><path d="M5 0a3.5 3.5 0 0 0-3.5 3.5C1.5 6 5 10 5 10s3.5-4 3.5-6.5A3.5 3.5 0 0 0 5 0zm0 5a1.5 1.5 0 1 1 0-3 1.5 1.5 0 0 1 0 3z"/></svg>
            2861 Corvella Parkway 318-742 San Jose, California 95342
          </span>
        </div>
        <div class="contact-line">
          <span class="contact-item">
            <svg class="contact-icon" viewBox="0 0 10 10"><path d="M2 0l2 2.5-1.2 1.2a6 6 0 0 0 3.5 3.5L7.5 6 10 8l-1.5 2C4 10 0 6 0 1.5z"/></svg>
            408-297-1586
          </span>
          <span class="contact-item">
            <svg class="contact-icon" viewBox="0 0 10 10"><rect x="2" y="0" width="6" height="3"/><rect x="0" y="3.5" width="10" height="4.5" rx="1"/><rect x="2" y="8" width="6" height="2"/></svg>
            408-853-2941
          </span>
        </div>
        <div class="contact-line">
          <span class="contact-item">
            <svg class="contact-icon" viewBox="0 0 10 10"><path d="M0 2h10v6H0z M0 2l5 3.5L10 2" fill="none" stroke="#5f7a8c" stroke-width="1.2"/></svg>
            emil@qrnlegalgroup.example
          </span>
          <span class="contact-item">
            <svg class="contact-icon" viewBox="0 0 10 10"><circle cx="5" cy="5" r="4.3" fill="none" stroke="#5f7a8c" stroke-width="1.2"/><path d="M0.7 5h8.6M5 0.7c-2.4 2.6-2.4 6 0 8.6M5 0.7c2.4 2.6 2.4 6 0 8.6" fill="none" stroke="#5f7a8c" stroke-width="0.8"/></svg>
            www.qrnlegalgroup.example
          </span>
        </div>
      </div>
    </header>

    <svg class="footer-wave" viewBox="0 0 560 140" preserveAspectRatio="none" aria-hidden="true">
      <defs>
        <linearGradient id="silverSweep" x1="0" y1="0" x2="1" y2="0">
          <stop offset="0" stop-color="var(--silver-dark)"/>
          <stop offset="0.45" stop-color="var(--silver-light)"/>
          <stop offset="1" stop-color="var(--silver-dark)"/>
        </linearGradient>
      </defs>
      <path d="M0 0 C60 6 140 40 220 82 C320 128 440 136 560 140 L0 140 Z" fill="url(#silverSweep)"/>
      <path d="M0 3 C40 12 80 26 110 52 C160 96 260 132 560 140 L0 140 Z" fill="var(--slate)"/>
      <line x1="0" y1="1" x2="60" y2="5" stroke="var(--slate-dark)" stroke-width="1.5"/>
    </svg>
  </main>
</body>
</html>
```